Beer Label

We need a design for our new beer label. It needs to be slick, but there is one little catch. The logo of the brand was made by the client, and in our humble opinion it is not very esthetic.

The bottle is ambar dark so we need to be smart with the colors. The beer is made essentially from HONEY (its a HONEY LAGER).

So attached is the logo of the brand, we need to have in the design the regular information of a beer:

"Producida y Embasada en Republica Dominicana"
"4% alcohol"

Font styles to use
Script

Requirements
Must have
• There must be the regular label and the small one on the neck of the bottle that matches the design.

```html
<!DOCTYPE html>
<html lang="es">
<head>
<meta charset="utf-8">
<title>Sol de Miel – Honey Lager</title>
<link href="https://fonts.googleapis.com/css2?family=Montserrat:wght@500;700;800&family=Tinos:ital@1&display=swap" rel="stylesheet">
<style>
  :root {
    --backdrop: #eceef0;
    --label-brown: #5a2207;
    --honey-yellow: #ece95c;
    --honey-orange: #f2a31b;
    --honey-light: #f8cf5a;
    --strip-black: #1c1a1a;
    --strip-text: #f4f1e6;
  }
  * { box-sizing: border-box; margin: 0; padding: 0; }
  html, body { width: 848px; height: 1200px; overflow: hidden; }
  body {
    background: var(--backdrop);
    position: relative;
    font-family: "Montserrat", Arial, sans-serif;
  }
  .neck-label {
    position: absolute;
    left: 304px;
    top: 120px;
    width: 240px;
    height: 320px;
  }
  .main-label {
    position: absolute;
    left: 232px;
    top: 560px;
    width: 384px;
    height: 430px;
  }
  .brand-name {
    font-family: "Montserrat", Arial, sans-serif;
    font-weight: 800;
    fill: var(--label-brown);
    letter-spacing: 1px;
  }
  .since-line {
    font-family: "Montserrat", Arial, sans-serif;
    font-weight: 500;
    fill: var(--label-brown);
  }
  .origin-text {
    font-family: "Tinos", "Times New Roman", serif;
    font-style: italic;
    fill: var(--strip-text);
  }
  .abv-text {
    font-family: "Montserrat", Arial, sans-serif;
    font-weight: 500;
    fill: var(--honey-yellow);
  }
  .style-name {
    font-family: "Montserrat", Arial, sans-serif;
    font-weight: 700;
    fill: var(--honey-yellow);
    letter-spacing: 2px;
  }
</style>
</head>
<body>

  <!-- Neck label -->
  <svg class="neck-label" viewBox="0 0 240 320" xmlns="http://www.w3.org/2000/svg">
    <defs>
      <path id="neck-brand-arc" d="M26,160 Q120,128 214,160"/>
    </defs>
    <rect role="img" aria-label="Slim vertical flourish ornament above the band" x="108" y="0" width="24" height="118" rx="12" fill="var(--honey-yellow)" opacity="0.55"/>
    <path class="neck-band" d="M20,150 Q120,100 220,150 L220,198 Q120,150 20,198 Z" fill="var(--honey-yellow)"/>
    <text class="brand-name" font-size="21" text-anchor="middle">
      <textPath href="#neck-brand-arc" startOffset="50%">SOL DE MIEL</textPath>
    </text>
    <line x1="68" y1="165" x2="92" y2="165" stroke="var(--label-brown)" stroke-width="0.8"/>
    <line x1="148" y1="165" x2="172" y2="165" stroke="var(--label-brown)" stroke-width="0.8"/>
    <text class="since-line" x="120" y="168" font-size="8" text-anchor="middle">Desde 1989</text>
    <rect role="img" aria-label="Slim vertical flourish ornament below the band" x="108" y="200" width="24" height="118" rx="12" fill="var(--honey-yellow)" opacity="0.55"/>
  </svg>

  <!-- Main body label -->
  <svg class="main-label" viewBox="0 0 384 430" xmlns="http://www.w3.org/2000/svg">
    <defs>
      <clipPath id="label-shape">
        <rect x="0" y="0" width="384" height="430" rx="26"/>
      </clipPath>
      <linearGradient id="honey-foam" x1="0" y1="0" x2="0" y2="1">
        <stop offset="0" stop-color="var(--honey-light)"/>
        <stop offset="1" stop-color="var(--honey-orange)"/>
      </linearGradient>
      <path id="brand-arc" d="M14,208 Q192,142 370,208"/>
      <path id="since-arc" d="M90,212 Q192,196 294,212"/>
    </defs>
    <g clip-path="url(#label-shape)">
      <rect class="label-body" x="0" y="0" width="384" height="430" fill="var(--label-brown)"/>
      <path role="img" aria-label="Honey foam band with bubble pattern" d="M0,0 H384 V44 Q350,36 330,44 Q300,52 260,40 Q220,30 192,38 Q150,48 110,38 Q70,30 40,42 Q20,48 0,40 Z" fill="url(#honey-foam)"/>
      <rect role="img" aria-label="Symmetric flower flourish ornament" x="72" y="44" width="240" height="50" rx="25" fill="var(--honey-yellow)" opacity="0.35"/>
      <path class="title-band" d="M0,150 Q192,50 384,150 L384,300 Q192,290 0,300 Z" fill="var(--honey-yellow)"/>
      <text class="brand-name" font-size="42" text-anchor="middle">
        <textPath href="#brand-arc" startOffset="50%">SOL DE MIEL</textPath>
      </text>
      <line x1="96" y1="203" x2="136" y2="201" stroke="var(--label-brown)" stroke-width="1"/>
      <line x1="248" y1="201" x2="288" y2="203" stroke="var(--label-brown)" stroke-width="1"/>
      <text class="since-line" font-size="15" text-anchor="middle">
        <textPath href="#since-arc" startOffset="50%">Desde 1989</textPath>
      </text>
      <rect role="img" aria-label="Symmetric flower flourish ornament" x="72" y="236" width="240" height="50" rx="25" fill="var(--label-brown)" opacity="0.35"/>
      <rect class="origin-strip" x="24" y="340" width="272" height="22" fill="var(--strip-black)"/>
      <text class="origin-text" x="30" y="356" font-size="11.5" textLength="260" lengthAdjust="spacingAndGlyphs">Producida y Embasada en Republica Dominicana"</text>
      <text class="abv-text" x="306" y="376" font-size="11">4% alcohol</text>
      <text class="style-name" x="192" y="412" font-size="24" text-anchor="middle">HONEY LAGER</text>
    </g>
  </svg>

</body>
</html>
```